Coralith Partners's New Branding
Anything the customer sees, we want to update
Coralith Partners's New Branding -
Creative Brief
Professional
Dorian Pelk, MCP
Director of Technology
418 West Alder Road Morton, IL 61552
dorian.pelk@coralithpt.example
www.coralithpt.example
In addition to branding our business cards, we're also looking to brand: 1) folders - two pockets w/ a slotted area on the left pocket to insert a business card 2) brochures - 8.5"x11" tri-fold brochure 3) letterhead 4) envelopes 5) sales proposal cover letter - Our logo and name - Presented to: "Customer's name" - Presented by: "our sales person(s)" - Title of presentation - our web address 6) powerpoint 7) binders (including spline) 8) cd label - Company's name we're presenting cd to - our logo and name - title of content on cd
Quote: "Our business is sustaining yours" Please layout the quote so that if we put a QR code on the back of the card in the future, it won't look out of place.

```html
<!DOCTYPE html>
<html lang="en">
<head>
<meta charset="utf-8">
<title>Coralith Partners Presentation Folder</title>
<link href="https://fonts.googleapis.com/css2?family=Open+Sans:wght@400;600;700&display=swap" rel="stylesheet">
<style>
  :root {
    --green-deep: #1d6b2a;
    --green: #2e8b3a;
    --green-light: #5cb85c;
    --paper: #ffffff;
    --backdrop: #e4e4e4;
    --rule: #cccccc;
    --text-light: #eaf6ea;
  }
  * { box-sizing: border-box; margin: 0; padding: 0; }
  html, body { width: 1200px; height: 871px; overflow: hidden; }
  body {
    background: var(--backdrop);
    font-family: "Open Sans", Arial, sans-serif;
    position: relative;
  }
  .spread {
    position: absolute;
    top: 245px;
    width: 520px;
    height: 380px;
    display: flex;
    box-shadow: 0 6px 18px rgba(0,0,0,.25);
  }
  .spread--outside { left: 50px; }
  .spread--inside { left: 630px; }
  .panel { position: relative; width: 50%; height: 100%; overflow: hidden; }
  .panel--green {
    background: linear-gradient(160deg, var(--green-light) 0%, var(--green) 45%, var(--green-deep) 100%);
    color: var(--text-light);
  }
  .panel--white { background: var(--paper); }
  .brand {
    position: absolute;
    display: flex; align-items: center; gap: 6px;
    font-weight: 700; font-size: 12px; letter-spacing: .5px;
    text-transform: uppercase; white-space: nowrap;
  }
  .brand__dot { width: 14px; height: 14px; border-radius: 50%; background: currentColor; }
  .brand--light { color: var(--paper); }
  .brand--green { color: var(--green-deep); }
  .brand--small { font-size: 9px; }
  .brand--small .brand__dot { width: 10px; height: 10px; }
  .web { position: absolute; font-size: 9px; font-weight: 600; color: var(--paper); white-space: nowrap; }
  .tagline { position: absolute; font-size: 9px; color: var(--paper); white-space: nowrap; }
  .contact {
    position: absolute; right: 16px; bottom: 80px;
    font-size: 6.5px; line-height: 1.55; color: var(--text-light); text-align: right;
  }
  .world-map {
    position: absolute; left: 20px; top: 90px; width: 220px; height: 170px;
    border-radius: 40%;
    background: radial-gradient(ellipse at center, rgba(255,255,255,.14), rgba(255,255,255,0) 70%);
  }
  .pocket { position: absolute; left: 0; right: 0; bottom: 0; height: 150px; }
  .pocket--white { border-top: 1px solid #ddd; background: #fbfbfb; }
  .pocket--green {
    background: linear-gradient(160deg, var(--green) 0%, var(--green-deep) 100%);
    border-top: 1px solid rgba(255,255,255,.35);
  }
  .card-slot { position: absolute; left: 70px; top: 40px; width: 120px; height: 1px; background: var(--rule); }
  .card-slot--lower { top: 110px; }
</style>
</head>
<body>
  <section class="spread spread--outside" aria-label="Folder outside">
    <div class="panel panel--green">
      <div class="contact">
        Dorian Pelk, MCP<br>Director of Technology<br>418 West Alder Road Morton, IL 61552<br>dorian.pelk@coralithpt.example
      </div>
      <p class="web" style="left:18px;bottom:48px;">www.coralithpt.example</p>
      <div class="brand brand--light brand--small" style="right:16px;bottom:20px;">
        <span class="brand__dot"></span>Coralith Partners
      </div>
    </div>
    <div class="panel panel--green">
      <div class="world-map" role="img" aria-label="Faint world map in light green tones"></div>
      <div class="brand brand--light" style="left:20px;top:26px;">
        <span class="brand__dot"></span>Coralith Partners
      </div>
      <p class="tagline" style="left:20px;bottom:24px;">Our business is sustaining yours</p>
    </div>
  </section>

  <section class="spread spread--inside" aria-label="Folder inside">
    <div class="panel panel--white">
      <div class="brand brand--green" style="left:70px;top:120px;">
        <span class="brand__dot"></span>Coralith Partners
      </div>
      <div class="pocket pocket--white">
        <span class="card-slot"></span>
        <span class="card-slot card-slot--lower"></span>
      </div>
    </div>
    <div class="panel panel--green">
      <p class="tagline" style="left:20px;top:24px;">Our business is sustaining yours</p>
      <div class="pocket pocket--green">
        <div class="brand brand--light" style="right:20px;top:40px;">
          <span class="brand__dot"></span>Coralith Partners
        </div>
        <p class="web" style="left:20px;bottom:20px;">www.coralithpt.example</p>
      </div>
    </div>
  </section>
</body>
</html>
```